Dane Calloway Photography

Would like the Business card to have a cool logo. I’m targeting wedding/ engagement: portrait photography. My phone number on it. And my business email address.

Target Market(s)

Wedding/portrait/engagement photography.

```html
<!DOCTYPE html>
<html lang="en">
<head>
<meta charset="utf-8">
<title>Dane Calloway Photography – Business Card</title>
<link rel="stylesheet" href="https://fonts.googleapis.com/css2?family=Jost:wght@400;500&display=swap">
<style>
  :root {
    --stage: #3a3a3a;
    --paper: #f1f2f2;
    --paper-shade: #dfe1e2;
    --ink: #1c1c1c;
    --band: #1b1b1b;
    --accent: #d92a27;
    --on-band: #f4f4f4;
    --rule: #5a5a5a;
  }
  * { box-sizing: border-box; margin: 0; padding: 0; }
  html, body {
    width: 1200px;
    height: 659px;
    overflow: hidden;
    background: var(--stage);
    font-family: "Jost", sans-serif;
  }
  .stage {
    position: relative;
    width: 1200px;
    height: 659px;
    display: flex;
    align-items: center;
    justify-content: center;
    gap: 60px;
  }
  .card {
    position: relative;
    width: 520px;
    height: 297px;
    overflow: hidden;
    box-shadow: 0 10px 30px rgba(0,0,0,.45);
  }
  .card__texture {
    position: absolute;
    inset: 0;
    background: linear-gradient(170deg, var(--paper) 0%, #e9eaeb 55%, var(--paper-shade) 100%);
  }
  .brand {
    position: absolute;
    display: flex;
    align-items: center;
    gap: 12px;
    color: var(--ink);
    font-weight: 500;
    white-space: nowrap;
  }
  .brand__square {
    width: 22px;
    height: 22px;
    background: var(--accent);
    flex: none;
  }
  .card--back .brand {
    left: 50%;
    top: 50%;
    transform: translate(-50%, -50%);
    font-size: 30px;
  }
  .card--front .brand {
    left: 50%;
    top: 78px;
    transform: translateX(-50%);
    font-size: 28px;
  }
  .band {
    position: absolute;
    inset: 0;
  }
  .client-name {
    position: absolute;
    left: 44px;
    bottom: 46px;
    color: var(--on-band);
    font-size: 22px;
    font-weight: 400;
    letter-spacing: 1px;
    text-transform: uppercase;
  }
  .divider {
    position: absolute;
    left: 292px;
    bottom: 28px;
    width: 1px;
    height: 70px;
    background: var(--rule);
  }
  .contact {
    position: absolute;
    left: 312px;
    bottom: 36px;
    list-style: none;
    color: var(--on-band);
    font-size: 14px;
    line-height: 1;
  }
  .contact__item {
    display: flex;
    align-items: center;
    gap: 10px;
    margin-top: 14px;
  }
  .contact__icon {
    width: 13px;
    height: 13px;
    flex: none;
    fill: var(--on-band);
  }
</style>
</head>
<body>
<main class="stage">

  <section class="card card--back" aria-label="Business card back">
    <div class="card__texture" role="img" aria-label="White-washed wood grain texture"></div>
    <div class="brand">
      <span class="brand__square"></span>
      <span class="brand__name">Dane Calloway Photography</span>
    </div>
  </section>

  <section class="card card--front" aria-label="Business card front">
    <div class="card__texture" role="img" aria-label="White-washed wood grain texture"></div>
    <div class="brand">
      <span class="brand__square"></span>
      <span class="brand__name">Dane Calloway Photography</span>
    </div>
    <svg class="band" viewBox="0 0 520 297" preserveAspectRatio="none" aria-hidden="true">
      <path d="M0 225 C110 170 190 160 300 150 C390 142 460 120 520 88 L520 297 L0 297 Z" fill="var(--band)"/>
    </svg>
    <p class="client-name">Client Name</p>
    <span class="divider"></span>
    <ul class="contact">
      <li class="contact__item">
        <svg class="contact__icon" viewBox="0 0 24 24" aria-hidden="true">
          <path d="M6.6 10.8a15.1 15.1 0 0 0 6.6 6.6l2.2-2.2a1 1 0 0 1 1-.25 11.4 11.4 0 0 0 3.6.57 1 1 0 0 1 1 1V20a1 1 0 0 1-1 1A17 17 0 0 1 3 4a1 1 0 0 1 1-1h3.5a1 1 0 0 1 1 1c0 1.25.2 2.45.57 3.6a1 1 0 0 1-.25 1z"/>
        </svg>
        <span>555.010.2048</span>
      </li>
      <li class="contact__item">
        <svg class="contact__icon" viewBox="0 0 24 24" aria-hidden="true">
          <path d="M2 5h20v14H2z M3.5 6.5v.4l8.5 6 8.5-6v-.4z" fill-rule="evenodd"/>
        </svg>
        <span>hello@danecallowayphoto.com</span>
      </li>
    </ul>
  </section>

</main>
</body>
</html>
```